Modern claims management company

We need a new company presentation brochure, composed of about 20 pages in A4 format.
Cover, page 1 who we are, page 2 company profile, page 3 territorial operation, page from 4 to 10 services offered and description of services (The title of the page are: Perizie e Liquidazione danni, riparazioni e sostituzioni, teleclaimer, accertamento danni da fenomeno elettrico, TPA, Auditing, drone pilot, Valutazione rischi), from 11 to 17 specializations (Sinistri gravi, R.C., Tecnologici, Energie rinnovabili, strutture, ambiente) page 18 e 19 integrated services (perdite occulte, ricerca guasti, indagini termografiche, crisis management), page 20 clients ( list companies and logos) page 21 contact.
The company is made up of various companies, which belong to the principal, each of which deals with specific activities.
To date we already have various logos of the main company (Vardano and Pescetti) as well as the logos of the other companies. I load them on the portal.
Found then the graphic solution that we like we will have to proceed to make a presentation in similar powerpoint and the website.

Target Market(s)

Insurance Company, Insurance Broker

Font styles to use
Other font styles liked:
• ARIAL

Colors
333333
5c5c5c
959595
0392cd

Requirements
Must have
• It must be clear, professional and modern.
Nice to have
• I indicate some competitor sites, so that you can better understand what we are doing. www.torvellsgroup.example, www.harbridgeoakes.example, www.betadomaretti.example, www.gruppotavesi.example, www.vantuzzi.example.

```html
<!DOCTYPE html>
<html lang="en">
<head>
<meta charset="utf-8">
<title>Vardano and Pescetti – Territorial operation</title>
<link href="https://fonts.googleapis.com/css2?family=Arimo:wght@400;700&display=swap" rel="stylesheet">
<style>
  :root {
    --frame-dark: #333333;
    --frame-mid: #5c5c5c;
    --steel-dark: #959595;
    --steel-light: #e4e4e4;
    --brand-blue: #0392cd;
    --bar-blue: #1577c4;
    --ink: #111111;
    --white: #ffffff;
  }
  html, body {
    margin: 0;
    padding: 0;
    overflow: hidden;
  }
  body {
    width: 847px;
    height: 1200px;
    background: linear-gradient(180deg, var(--frame-mid) 0%, var(--frame-dark) 50%, var(--frame-mid) 100%);
    font-family: "Arimo", Arial, sans-serif;
    position: relative;
  }
  .page {
    position: absolute;
    left: 20px;
    top: 20px;
    width: 807px;
    height: 1160px;
    background:
      repeating-linear-gradient(180deg, rgba(255,255,255,0.10) 0px, rgba(255,255,255,0.10) 1px, rgba(0,0,0,0.05) 2px, rgba(0,0,0,0) 3px),
      linear-gradient(170deg, #a6a6a6 0%, #c8c8c8 35%, var(--steel-dark) 60%, var(--steel-light) 100%);
    box-shadow: 0 0 6px rgba(0,0,0,0.6);
  }
  .brand-name {
    position: absolute;
    left: 18px;
    top: 30px;
    margin: 0;
    font-size: 34px;
    font-weight: 400;
    color: var(--brand-blue);
    letter-spacing: 0.5px;
  }
  .section-bar {
    position: absolute;
    left: 408px;
    top: 58px;
    width: 398px;
    height: 32px;
    background: linear-gradient(180deg, #2a8ad6 0%, var(--bar-blue) 60%, #0f64a8 100%);
    color: var(--white);
    font-size: 23px;
    line-height: 32px;
    text-align: center;
    margin: 0;
    font-weight: 400;
  }
  .content {
    position: absolute;
    left: 22px;
    top: 140px;
    width: 770px;
    font-size: 15.2px;
    line-height: 18px;
    color: var(--ink);
  }
  .content p {
    margin: 0 0 26px 0;
  }
  .content p.lead {
    margin-bottom: 26px;
  }
  .content p.item::before {
    content: "";
    display: inline-block;
    width: 13px;
    height: 13px;
    margin: 0 12px 0 -2px;
    vertical-align: -1px;
    background: var(--bar-blue);
    box-shadow: inset 0 0 0 1px #0d4f88;
  }
  .page-number {
    position: absolute;
    right: 20px;
    bottom: 22px;
    margin: 0;
    font-size: 16px;
    color: var(--ink);
  }
</style>
</head>
<body>
  <main class="page">
    <header>
      <p class="brand-name">Vardano and Pescetti</p>
      <h1 class="section-bar">Territorial operation</h1>
    </header>

    <section class="content">
      <p class="lead">Sed ut perspiciatis unde omnis iste natus isisa error sit voluptatem accusantium doloremque architecto laudantium, totam rem aperiam,eaque ipsa po quae ab illo inventore veritatis et quasi delmas architecto architecto beatae vitae dicta sunt explicabo. Nemo enim ipsam voluptatem quia voluptas sit aspernatur aut odit aut fugit, sed quia consequuntur magni dolores eos qui ratione voluptatem sequi nesciunt. Mita Neque porro quisquam est, qui dolorem ipsum quia dolor sit amet, consectetur, adipisci velit, sed quia non numquam eius modi tempora incidunt ut labore et dolore magnam aliquam quaerat voluptatem. Re Ut enim ad minima veniam, quis nostrum exercitationem ullam corporis suscipit laboriosam, nisi ut eine aliquid ex ea commodi consequatur? Quis autem vel eum iure reprehenderit qui in ea voluptate velit for esse quam nihil molestiae consequatur, vel illum qui dolorem eum fugiat quo voluptas nulla pariatur?"</p>

      <p class="item">At perspiciatis unde omnis iste natus isisa error sit voluptatem accusantium doloremque architecto laudantium, totam rem aperiam,eaque ipsa po quae ab illo inventore veritatis et quasi delmas architecto architecto beatae vitae dicta sunt explicabo. Nemo enim ipsam voluptatem quia voluptas sit aspernatur aut odit aut fugit, sed quia consequuntur magni dolores eos qui ratione voluptatem sequi nesciunt. Mita Neque porro quisquam est, qui dolorem ipsum quia dolor sit amet, consectetur, adipisci velit, sed quia non numquam eius modi tempora incidunt ut labore et dolore magnam aliquam quaerat voluptatem. Re Ut enim ad minima veniam, quis nostrum exercitationem ullam corporis suscipit laboriosam, nisi ut eine aliquid ex ea commodi consequatur? Quis autem vel eum iure reprehenderit qui in ea voluptate velit for esse quam nihil molestiae consequatur, vel illum qui dolorem eum fugiat quo voluptas nulla pariatur?"</p>

      <p class="item">At perspiciatis unde omnis iste natus isisa error sit voluptatem accusantium doloremque architecto laudantium, totam rem aperiam,eaque ipsa po quae ab illo inventore veritatis et quasi delmas architecto architecto beatae vitae dicta sunt explicabo. Nemo enim ipsam voluptatem quia voluptas sit aspernatur aut odit aut fugit, sed quia consequuntur magni dolores eos qui ratione voluptatem sequi nesciunt. Mita</p>

      <p class="item">At perspiciatis unde omnis iste natus isisa error sit voluptatem accusantium doloremque architecto laudantium, totam rem aperiam,eaque ipsa po quae ab illo inventore veritatis et quasi delmas architecto architecto beatae vitae dicta sunt explicabo. Nemo enim ipsam voluptatem quia voluptas sit aspernatur aut odit aut fugit, sed quia consequuntur magni dolores eos qui ratione voluptatem sequi nesciunt. Mita Neque porro quisquam est, qui dolorem ipsum quia dolor sit amet, consectetur, adipisci velit, sed quia non numquam eius modi tempora incidunt ut labore et dolore magnam aliquam quaerat voluptatem. Re Ut enim ad minima veniam, quis nostrum exercitationem ullam corporis suscipit laboriosam, nisi ut eine aliquid ex ea commodi consequatur? Quis autem vel eum iure reprehenderit qui in ea voluptate velit for esse quam nihil molestiae consequatur, vel illum qui dolorem eum fugiat quo voluptas nulla pariatur?"</p>

      <p class="item">At perspiciatis unde omnis iste natus isisa error sit voluptatem accusantium doloremque architecto laudantium, totam rem aperiam,eaque ipsa po quae ab illo inventore veritatis et quasi delmas architecto architecto beatae vitae dicta sunt explicabo. Nemo enim ipsam voluptatem quia voluptas sit aspernatur aut odit aut fugit, sed quia consequuntur magni dolores eos qui ratione voluptatem sequi nesciunt. Mita Neque porro quisquam est, qui dolorem ipsum quia dolor sit amet, consectetur, adipisci velit, sed quia non numquam eius modi tempora incidunt ut labore et dolore magnam aliquam quaerat voluptatem. Re Ut enim ad minima veniam, quis nostrum exercitationem ullam corporis suscipit laboriosam, nisi ut eine aliquid ex ea commodi consequatur? Quis autem vel eum iure reprehenderit qui in ea voluptate velit for esse quam nihil molestiae consequatur, vel illum qui dolorem eum fugiat quo voluptas nulla pariatur?"</p>
    </section>

    <p class="page-number">Page 3</p>
  </main>
</body>
</html>
```